Retail healthy snack bar design

We are launching a new product range to be sold in health food stores.

The Vorla Co (no logo as yet).

We will have a range of bars, spreads (jars), shakes (bags) in the following ranges-
milk protein
plant protein
keto

For this project, please do a bar design. The chosen designer will be given additional work for the rest of the packaging as well as promotional material such as social media, banners, posters etc.

Brisk Stick Protein - Must be White to be recognized.
Brisk Stick Collagen - Bronze
Brisk Keto Stick - Possibly Red
Brisk Stick Plant - Green

Food images can be added but their must be samples without as we may need to remove for certain countries.

Target Market(s)

Healthy, Weight-loss, Bodybuilding, Elderly, Medical

Industry/Entity Type

Health And Wellness

Font styles to use
Sans Serif

Colors

Designer to choose colors to be used in the design.

Requirements
Must have
• Clean simple to read design with minimal colours

Flavour to be easily read (Must include the word 'Flavour' in the same size font as the flavour description)

Must show size of bar (60g).

Some details that can be added (optional)-
raw, cold pressed bar with (example) whey protein isolate + prebiotic fibre
natural, with no artificial colours, flavours, preservatives or sweeteners
no added sugar or sugar alcohols - gluten free - soy free

Rear of bar shall remain the same or all same details if redesigned.
Nice to have
• Clean design, use of silver foil and/or matt/gloss affect, large oversized flavour image (if including).

See images of current designs I like on the market for ideas
Should not have
• Too many images (if any).

```html
<!DOCTYPE html>
<html lang="en">
<head>
<meta charset="utf-8">
<title>Brisk Bars – Paleo and Ketone</title>
<link href="https://fonts.googleapis.com/css2?family=Montserrat:wght@600;800;900&family=Oswald:wght@500&display=swap" rel="stylesheet">
<style>
  :root {
    --bg-top: #dfe8ee;
    --bg-bottom: #f4f6f7;
    --wrapper-black: #0b0b0b;
    --white: #ffffff;
    --paleo-green: #2a5d12;
    --paleo-yellow: #f5c518;
    --paleo-food-a: #f7d21a;
    --paleo-food-b: #e9a817;
    --keto-red: #b8102a;
    --keto-food-a: #e8132b;
    --keto-food-b: #a90d1f;
  }
  * { margin: 0; padding: 0; box-sizing: border-box; }
  html, body { width: 1200px; height: 1056px; overflow: hidden; }
  body {
    background: linear-gradient(180deg, var(--bg-top), var(--bg-bottom));
    font-family: "Montserrat", Arial, sans-serif;
    position: relative;
  }
  .bar {
    position: absolute;
    left: 120px;
    width: 960px;
    height: 320px;
  }
  .bar--paleo { top: 110px; --pill: var(--paleo-yellow); --pill-text: var(--paleo-green); --claim: var(--paleo-yellow); }
  .bar--ketone { top: 600px; --pill: var(--keto-red); --pill-text: var(--white); --claim: var(--keto-red); }
  .bar__shape { position: absolute; inset: 0; }
  .bar__claims {
    position: absolute;
    left: 170px;
    top: 44px;
    font-weight: 600;
    font-size: 13px;
    line-height: 17px;
    letter-spacing: 0.3px;
    color: var(--white);
  }
  .bar--paleo .claim--natural { color: var(--paleo-yellow); }
  .bar--ketone .claim--intro { color: var(--keto-red); }
  .bar__name {
    position: absolute;
    left: 160px;
    top: 96px;
    font-weight: 900;
    font-size: 150px;
    line-height: 1;
    letter-spacing: -2px;
    color: var(--white);
  }
  .bar__size {
    position: absolute;
    left: 62px;
    top: 142px;
    font-weight: 800;
    font-size: 28px;
    line-height: 1;
    color: var(--white);
  }
  .bar__variant {
    position: absolute;
    left: 448px;
    top: 244px;
    background: var(--pill);
    color: var(--pill-text);
    font-weight: 800;
    font-size: 22px;
    line-height: 30px;
    padding: 4px 24px;
    border-radius: 20px;
    letter-spacing: 1px;
    white-space: nowrap;
  }
  .bar__diet {
    position: absolute;
    right: 530px;
    top: 250px;
    font-weight: 600;
    font-size: 13px;
    line-height: 17px;
    color: var(--claim);
    text-align: right;
    white-space: nowrap;
  }
  .bar--ketone .bar__diet { color: var(--white); }
  .badge-text {
    font-family: "Oswald", Arial, sans-serif;
    font-weight: 500;
  }
</style>
</head>
<body>

<section class="bar bar--paleo">
  <svg class="bar__shape" width="960" height="320" viewBox="0 0 960 320">
    <defs>
      <linearGradient id="paleo-food" x1="0" y1="0" x2="1" y2="1">
        <stop offset="0" stop-color="var(--paleo-food-a)"/>
        <stop offset="1" stop-color="var(--paleo-food-b)"/>
      </linearGradient>
    </defs>
    <polygon fill="var(--wrapper-black)" points="28,0 932,0 940,10 932,20 940,30 932,40 940,50 932,60 940,70 932,80 940,90 932,100 940,110 932,120 940,130 932,140 940,150 932,160 940,170 932,180 940,190 932,200 940,210 932,220 940,230 932,240 940,250 932,260 940,270 932,280 940,290 932,300 940,310 932,320 28,320 20,310 28,300 20,290 28,280 20,270 28,260 20,250 28,240 20,230 28,220 20,210 28,200 20,190 28,180 20,170 28,160 20,150 28,140 20,130 28,120 20,110 28,100 20,90 28,80 20,70 28,60 20,50 28,40 20,30 28,20 20,10"/>
    <polygon role="img" aria-label="Paleo bar ingredients close-up" fill="url(#paleo-food)" points="880,0 932,0 932,320 720,320 748,290 742,262 770,236 766,206 796,184 790,150 822,122 818,92 846,64 842,34"/>
    <g transform="translate(718,196)">
      <polygon points="0,0 64,0 32,56" fill="var(--white)"/>
      <text class="badge-text" x="32" y="16" font-size="13" fill="var(--paleo-green)" text-anchor="middle">SUGAR</text>
      <text class="badge-text" x="32" y="33" font-size="15" fill="var(--paleo-green)" text-anchor="middle">&lt;3g</text>
      <polygon points="68,56 100,0 132,56" fill="var(--paleo-green)"/>
      <text class="badge-text" x="100" y="38" font-size="15" fill="var(--white)" text-anchor="middle">&gt;20g</text>
      <text class="badge-text" x="100" y="51" font-size="10" fill="var(--white)" text-anchor="middle">PROTEIN</text>
      <polygon points="136,0 200,0 168,56" fill="var(--white)"/>
      <text class="badge-text" x="168" y="16" font-size="13" fill="var(--paleo-green)" text-anchor="middle">CARBS</text>
      <text class="badge-text" x="168" y="33" font-size="15" fill="var(--paleo-green)" text-anchor="middle">&lt;1g</text>
    </g>
  </svg>
  <p class="bar__claims">
    <span class="claim--intro">RAW, COLD PRESSED BAR<br>WITH WHEY PROTEIN ISOLATE + PREBIOTIC FIBRE</span><br>
    <span class="claim--natural">NATURAL, WITH NO ARTIFICIAL COLOURS, FLAVOURS, PRESERVATIVES OR SWEETENERS</span>
  </p>
  <span class="bar__size">60g</span>
  <h1 class="bar__name">BRISK</h1>
  <span class="bar__variant">PALEO FLAVOUR</span>
  <p class="bar__diet">NO ADDED SUGAR OR SUGAR ALCOHOLS<br>GLUTEN FREE - SOY FREE</p>
</section>

<section class="bar bar--ketone">
  <svg class="bar__shape" width="960" height="320" viewBox="0 0 960 320">
    <defs>
      <linearGradient id="keto-food" x1="0" y1="0" x2="1" y2="1">
        <stop offset="0" stop-color="var(--keto-food-a)"/>
        <stop offset="1" stop-color="var(--keto-food-b)"/>
      </linearGradient>
    </defs>
    <polygon fill="var(--wrapper-black)" points="28,0 932,0 940,10 932,20 940,30 932,40 940,50 932,60 940,70 932,80 940,90 932,100 940,110 932,120 940,130 932,140 940,150 932,160 940,170 932,180 940,190 932,200 940,210 932,220 940,230 932,240 940,250 932,260 940,270 932,280 940,290 932,300 940,310 932,320 28,320 20,310 28,300 20,290 28,280 20,270 28,260 20,250 28,240 20,230 28,220 20,210 28,200 20,190 28,180 20,170 28,160 20,150 28,140 20,130 28,120 20,110 28,100 20,90 28,80 20,70 28,60 20,50 28,40 20,30 28,20 20,10"/>
    <polygon role="img" aria-label="Ketone bar ingredients close-up" fill="url(#keto-food)" points="890,0 932,0 932,320 680,320 712,292 708,262 738,236 732,204 764,180 758,148 792,120 786,88 820,62 816,30 850,12"/>
    <g transform="translate(718,196)">
      <polygon points="0,0 64,0 32,56" fill="var(--white)"/>
      <text class="badge-text" x="32" y="16" font-size="13" fill="var(--keto-red)" text-anchor="middle">SUGAR</text>
      <text class="badge-text" x="32" y="33" font-size="15" fill="var(--keto-red)" text-anchor="middle">&lt;3g</text>
      <polygon points="68,56 100,0 132,56" fill="var(--white)"/>
      <text class="badge-text" x="100" y="38" font-size="15" fill="var(--keto-red)" text-anchor="middle">&gt;20g</text>
      <text class="badge-text" x="100" y="51" font-size="10" fill="var(--keto-red)" text-anchor="middle">PROTEIN</text>
      <polygon points="136,0 200,0 168,56" fill="var(--white)"/>
      <text class="badge-text" x="168" y="16" font-size="13" fill="var(--keto-red)" text-anchor="middle">CARBS</text>
      <text class="badge-text" x="168" y="33" font-size="15" fill="var(--keto-red)" text-anchor="middle">&lt;1g</text>
    </g>
  </svg>
  <p class="bar__claims">
    <span class="claim--intro">RAW, COLD PRESSED BAR<br>WITH WHEY PROTEIN ISOLATE + PREBIOTIC FIBRE</span><br>
    <span class="claim--natural">NATURAL, WITH NO ARTIFICIAL COLOURS, FLAVOURS, PRESERVATIVES OR SWEETENERS</span>
  </p>
  <span class="bar__size">60g</span>
  <h2 class="bar__name">BRISK</h2>
  <span class="bar__variant">KETONE FLAVOUR</span>
  <p class="bar__diet">NO ADDED SUGAR OR SUGAR ALCOHOLS<br>GLUTEN FREE - SOY FREE</p>
</section>

</body>
</html>
```